Brookmere Osteopathy flyer

I want a clean clear DL flyer (but also want an A4 poster) promoting a new Osteopathic business in a semi rural area in Tasmania (Australia).
It can have pictures like the examples attached to show people what Osteopathy is (its like Chiropractic and physiotherapy).
I am the sole practioner and am male, so any pictures would be best to be a white male if possible.
I've attached some wording, you can use all, or none of it
I don't have a phone number for the business yet
info@brookmereosteopathy.example
www.brookmereosteopathy.example
Target Market(s)
Australians, from tradies, professionals, babies to retired people
Industry/Entity Type
Health
Look and feel

```html
<!DOCTYPE html>
<html lang="en">
<head>
<meta charset="utf-8">
<title>Brookmere Osteopathy Flyer</title>
<link href="https://fonts.googleapis.com/css2?family=Montserrat:wght@400;600;700;800&family=Roboto+Slab:wght@400;600&family=Open+Sans:wght@300;700&family=Oswald:wght@500;600&display=swap" rel="stylesheet">
<style>
:root{
  --backdrop:#e9eef3;
  --paper:#ffffff;
  --orange:#ee6c22;
  --navy:#0f4fa3;
  --blue:#1a73c6;
  --sky:#18a4e0;
  --ink:#222222;
  --body:#333333;
  --grey:#444444;
}
*{margin:0;padding:0;box-sizing:border-box}
html,body{width:957px;height:1200px;overflow:hidden;background:var(--backdrop)}
.flyer{position:absolute;left:68px;top:25px;width:820px;height:1150px;background:var(--paper);overflow:hidden;box-shadow:0 4px 14px rgba(0,0,0,.18)}
.backdrop-art{position:absolute;inset:0}
.intro{position:absolute;left:38px;top:34px;font-family:"Roboto Slab",serif;font-size:20px;line-height:24px;color:var(--ink)}
.intro strong{font-weight:600}
.brand-seal{position:absolute;left:567px;top:27px;width:216px;height:216px;border-radius:50%;background:var(--paper);border:8px solid #e4e6ea;display:flex;align-items:center;justify-content:center;text-align:center;font-family:"Montserrat",sans-serif;font-weight:700;font-size:19px;line-height:24px;color:var(--sky)}
.photo{position:absolute;border-radius:50%;border:7px solid #eef0f3;box-shadow:0 3px 8px rgba(0,0,0,.2)}
.photo-back{left:252px;top:276px;width:224px;height:224px;background:radial-gradient(circle at 60% 60%,#e9b48d,#c98a63 45%,#5f7b88 80%)}
.photo-stretch{left:484px;top:324px;width:214px;height:214px;background:radial-gradient(circle at 45% 55%,#d9b59c,#9bb0c6 50%,#e6ecf2 85%)}
.photo-tennis{left:76px;top:900px;width:134px;height:134px;background:radial-gradient(circle at 50% 50%,#e6b89b,#7fa86a 60%,#c96a4a 95%)}
.photo-baby{left:190px;top:847px;width:204px;height:204px;background:radial-gradient(circle at 50% 40%,#f0c9b0,#b9c4d6 50%,#3d9ad1 85%)}
.headline{position:absolute;left:45px;top:534px;font-family:"Montserrat",sans-serif;font-weight:800;font-size:41px;line-height:42px;letter-spacing:-.5px}
.headline .orange{color:var(--orange)}
.headline .blue{color:var(--navy)}
.services-title{position:absolute;left:45px;top:640px;font-family:"Open Sans",sans-serif;font-weight:300;font-size:20px;color:var(--blue)}
.services{position:absolute;left:45px;top:684px;list-style:none;font-family:"Montserrat",sans-serif;font-weight:700;font-size:15px;line-height:21.2px;color:var(--ink)}
.services li{display:flex;align-items:center;gap:7px}
.services svg{width:14px;height:14px;flex:none}
.divider{position:absolute;left:378px;top:568px;width:1px;height:322px;background:#d9dde2}
.about{position:absolute;left:408px;top:582px;width:362px;font-family:"Montserrat",sans-serif;font-size:13px;line-height:21.4px;color:var(--body)}
.about strong{color:#111;font-weight:700}
.rule{position:absolute;left:408px;top:787px;width:347px;height:2px;background:var(--orange)}
.wordmark{position:absolute;left:405px;top:820px;width:352px;height:168px}
.wordmark text{font-family:"Oswald",sans-serif;font-weight:600}
.website{position:absolute;left:408px;top:1003px;width:347px;text-align:center;font-family:"Open Sans",sans-serif;font-weight:700;font-size:18.5px;color:var(--grey)}
.phone{position:absolute;left:40px;top:1060px;display:flex;align-items:center;gap:8px;font-family:"Oswald",sans-serif;font-weight:500;font-size:33px;color:#fff;line-height:1}
.phone svg{width:34px;height:34px}
.email{position:absolute;left:41px;top:1100px;font-family:"Montserrat",sans-serif;font-weight:700;font-size:13.5px;color:#fff}
.address{position:absolute;left:460px;top:1098px;font-family:"Montserrat",sans-serif;font-weight:700;font-size:14.5px;color:#fff}
</style>
</head>
<body>
<div class="flyer">
  <svg class="backdrop-art" viewBox="0 0 820 1150" width="820" height="1150">
    <defs>
      <linearGradient id="heroTone" x1="0" y1="0" x2="1" y2="1">
        <stop offset="0" stop-color="#f4ede8"/>
        <stop offset=".45" stop-color="#e7b89a"/>
        <stop offset=".8" stop-color="#d79f80"/>
        <stop offset="1" stop-color="#eef1f5"/>
      </linearGradient>
      <linearGradient id="bandTone" x1="0" y1="0" x2="1" y2="0">
        <stop offset="0" stop-color="#0f4fa3"/>
        <stop offset=".6" stop-color="#1d7fd0"/>
        <stop offset="1" stop-color="#16a6e0"/>
      </linearGradient>
    </defs>
    <path role="img" aria-label="Photo of an osteopath massaging a patient's upper back" d="M0 0H820V470C700 430 620 420 560 440C430 470 330 430 245 425C150 455 60 470 0 440Z" fill="url(#heroTone)"/>
    <path d="M0 445C80 480 170 470 245 425C160 470 80 495 0 485Z" fill="var(--navy)"/>
    <path d="M650 378C720 385 780 450 820 530V500C780 430 720 385 650 378Z" fill="var(--sky)"/>
    <path d="M0 930C60 915 100 925 130 935C250 980 380 1050 520 1050C640 1050 740 1010 820 985V1150H0Z" fill="url(#bandTone)"/>
    <path d="M0 925C60 910 100 918 130 928" stroke="#cfe7f7" stroke-width="5" fill="none"/>
    <path d="M420 1040C560 1075 700 1030 820 990" stroke="#7fd0f0" stroke-width="14" fill="none"/>
    <path d="M430 1030C570 1062 700 1020 820 982" stroke="#ffffff" stroke-width="5" fill="none"/>
  </svg>

  <p class="intro">Our new Osteopathic Services in<br><strong>Semi Rural area in Tasmania (Australia)</strong></p>

  <div class="brand-seal">Brookmere<br>Osteopathy</div>

  <div class="photo photo-back" role="img" aria-label="Photo of hands treating a patient's lower back"></div>
  <div class="photo photo-stretch" role="img" aria-label="Photo of a patient receiving a shoulder stretch on a treatment table"></div>

  <h1 class="headline"><span class="orange">Move better,</span><br><span class="blue">Feel better.</span></h1>

  <h2 class="services-title">Our Services are:</h2>
  <ul class="services">
    <li><svg viewBox="0 0 14 14"><path d="M1 7.5l4 4L13 2" stroke="#ee6c22" stroke-width="2.4" fill="none"/></svg>Back / neck pain</li>
    <li><svg viewBox="0 0 14 14"><path d="M1 7.5l4 4L13 2" stroke="#ee6c22" stroke-width="2.4" fill="none"/></svg>Headaches / migraines</li>
    <li><svg viewBox="0 0 14 14"><path d="M1 7.5l4 4L13 2" stroke="#ee6c22" stroke-width="2.4" fill="none"/></svg>Joint and muscle pain</li>
    <li><svg viewBox="0 0 14 14"><path d="M1 7.5l4 4L13 2" stroke="#ee6c22" stroke-width="2.4" fill="none"/></svg>Pregnancy-related discomfort</li>
    <li><svg viewBox="0 0 14 14"><path d="M1 7.5l4 4L13 2" stroke="#ee6c22" stroke-width="2.4" fill="none"/></svg>Disc related issues</li>
    <li><svg viewBox="0 0 14 14"><path d="M1 7.5l4 4L13 2" stroke="#ee6c22" stroke-width="2.4" fill="none"/></svg>Adhesive capsulitis (frozen shoulder)</li>
    <li><svg viewBox="0 0 14 14"><path d="M1 7.5l4 4L13 2" stroke="#ee6c22" stroke-width="2.4" fill="none"/></svg>Tennis / Golfers elbow</li>
    <li><svg viewBox="0 0 14 14"><path d="M1 7.5l4 4L13 2" stroke="#ee6c22" stroke-width="2.4" fill="none"/></svg>Tendonitis / Bursitis</li>
    <li><svg viewBox="0 0 14 14"><path d="M1 7.5l4 4L13 2" stroke="#ee6c22" stroke-width="2.4" fill="none"/></svg>Plantar fasciitis</li>
    <li><svg viewBox="0 0 14 14"><path d="M1 7.5l4 4L13 2" stroke="#ee6c22" stroke-width="2.4" fill="none"/></svg>Sciatica</li>
  </ul>

  <div class="divider"></div>

  <p class="about">Brookmere Osteopathy use a tailored combination of <strong>joint mobilisation/manipulation</strong>, <strong>stretching, movement, trigger point dry needling and targeted massage</strong> to reduce pain and restore optimal function. Hands-on treatment is backed up with rehabilitative exercise prescription and advice. So whether you're recovering from injury or managing chronic discomfort, we're here to help you move better and feel your best.</p>

  <div class="rule"></div>

  <svg class="wordmark" viewBox="0 0 352 168" role="img" aria-label="Brookmere Osteopathy">
    <text x="0" y="84" font-size="104" fill="#0f4fa3" textLength="350" lengthAdjust="spacingAndGlyphs">BROOKMERE</text>
    <text x="0" y="165" font-size="104" fill="#ee6c22" textLength="342" lengthAdjust="spacingAndGlyphs">OSTEOPATHY</text>
  </svg>

  <p class="website">www.brookmereosteopathy.example</p>

  <div class="photo photo-tennis" role="img" aria-label="Photo of a tennis player holding her sore shoulder"></div>
  <div class="photo photo-baby" role="img" aria-label="Photo of a sleeping baby receiving gentle cranial treatment"></div>

  <div class="phone">
    <svg viewBox="0 0 34 34"><circle cx="17" cy="17" r="17" fill="#ee6c22"/><path d="M11 9c1-1 2-1 3 0l2 3c.5 1 .2 2-.6 2.6l-1 .8c1 2 2.6 3.6 4.6 4.6l.8-1c.6-.8 1.6-1.1 2.6-.6l3 2c1 1 1 2 0 3l-1.4 1.4C21 27 8 14 9.6 10.4Z" fill="#fff"/></svg>
    <span>03 6100 2468</span>
  </div>
  <p class="email">info@brookmereosteopathy.example</p>
  <p class="address">24 Wattle Creek Road, Brookmere</p>
</div>
</body>
</html>
```